IT supplier clean wordpress website - payment guaranteed

Clean website design for a wordpress based website
Design only - PSD delivery with images

current website: www.quilmo.net
please use your imagination and try something out of the box...
We like https://trevanly.com.au as look and feel, but you don't have to copy it, you can be creative

We like the navigation header and the phone number, but do not need 'instant quote' so the 1300 phone number and the 'lock' icon for login can be on the same line

Site Map:
IT support
VoIP
Internet and Data
Cloud hosting
About
Contact

Our logo is attached, it can be used light or dark.
Our only color used is the warm grey Pantone 8003C hex #877A69

You will only need to design the homepage to win the competition, but the winning designer will be required to supply without extra charges:
1. Home page design
2. A second, standard page template design
3. An icon set in colors appropriate to the site that have icons to match the subjects in these pages:
https://trevanly.com.au/products/
https://trevanly.com.au/making-the-switch/
https://trevanly.com.au/why-trevanly/
We will create a single page version of the options on https://trevanly.com.au/solutions/
4.Any images used

Please avoid stock photos that are too common - e.g. smiling woman with headset, try to make the design stand out with simple images and well-designed layout.

Mid-size business clients

It Company

1 page

• Veyra logo
• Use Veyra color

```html
<!DOCTYPE html>
<html lang="en">
<head>
<meta charset="utf-8">
<title>Veyra – do IT better</title>
<link rel="stylesheet" href="https://fonts.googleapis.com/css2?family=Open+Sans:wght@400;600;700;800&family=Exo+2:wght@500;600&display=swap">
<style>
:root{
  --warm-grey:#877a69;
  --warm-grey-dark:#6e6254;
  --orange:#e8862a;
  --ink:#3d352d;
  --text:#6b6460;
  --sand:#efebe5;
  --line:#ddd6cc;
  --footer:#2f2721;
  --footer-deep:#241e19;
  --white:#ffffff;
}
*{box-sizing:border-box;margin:0;padding:0}
html,body{width:1200px;height:2420px;overflow:hidden}
body{font-family:"Open Sans",Arial,sans-serif;color:var(--text);background:var(--white);font-size:14px}
a{color:inherit;text-decoration:none}

/* Header */
.site-header{height:68px;display:flex;align-items:center;padding:0 56px;background:var(--white);border-bottom:1px solid var(--line)}
.brand{font-family:"Open Sans",Arial,sans-serif;font-weight:700;font-size:24px;color:var(--warm-grey)}
.main-nav{display:flex;gap:26px;margin-left:80px;font-size:14px;font-weight:600;color:var(--ink)}
.header-contact{margin-left:auto;display:flex;align-items:center;gap:14px}
.phone{display:flex;align-items:center;gap:6px;font-weight:700;color:var(--ink);font-size:14px}
.login-btn{display:flex;align-items:center;gap:6px;background:var(--orange);color:var(--white);font-size:12px;font-weight:700;padding:7px 14px;border-radius:3px}

/* Hero */
.hero{position:relative;height:652px;overflow:hidden}
.hero-photo{position:absolute;inset:0;background:radial-gradient(ellipse at 50% 40%,#a9a08f 0%,#7d7564 45%,#4e4a3c 100%)}
.hero-title{position:absolute;left:0;right:0;top:470px;text-align:center;font-family:"Exo 2",Arial,sans-serif;font-weight:600;font-size:76px;color:var(--white);letter-spacing:1px}
.hero-dots{position:absolute;left:0;right:0;bottom:28px;display:flex;justify-content:center;gap:8px}
.hero-dots span{width:9px;height:9px;border-radius:50%;background:rgba(255,255,255,.5)}
.hero-dots span.active{background:var(--white)}

/* Section titles */
.section-title{display:flex;align-items:center;justify-content:center;gap:18px;font-weight:800;font-size:22px;color:var(--ink);letter-spacing:.5px}
.section-title::before,.section-title::after{content:"";width:40px;height:2px;background:var(--orange)}
.read-more{display:inline-block;color:var(--orange);font-size:11px;font-weight:700;letter-spacing:.5px}

/* Services */
.services{height:448px;background:var(--sand);padding-top:56px}
.service-grid{display:grid;grid-template-columns:repeat(4,1fr);gap:40px;padding:0 110px;margin-top:54px}
.service{text-align:center}
.service svg{height:90px;width:100px}
.service h3{font-size:15px;font-weight:700;color:var(--ink);margin:16px 0 10px}
.service p{font-size:12px;line-height:1.6;margin-bottom:12px}

/* Outsourcing */
.outsourcing{height:392px;padding:40px 110px 0;background:var(--white);border-top:14px solid var(--line)}
.outsourcing h2{font-size:21px;font-weight:800;color:var(--ink);letter-spacing:.3px}
.outsourcing h2::after{content:"";display:block;width:60px;height:3px;background:var(--orange);margin-top:10px}
.outsourcing-body{display:flex;gap:60px;margin-top:30px}
.outsourcing-copy{width:430px}
.outsourcing-copy h3{font-size:15px;font-weight:700;color:var(--ink);margin-bottom:12px}
.outsourcing-copy p{font-size:12.5px;line-height:1.65;margin-bottom:14px}
.btn-grey{display:inline-block;background:var(--warm-grey);color:var(--white);font-size:11px;font-weight:700;padding:8px 16px;border-radius:2px;margin-top:6px}
.video{position:relative;width:490px;height:270px;background:linear-gradient(135deg,#5d5548,#2f2b25 60%,#4a4339)}
.video .play{position:absolute;left:50%;top:50%;transform:translate(-50%,-50%)}

/* Products */
.products{height:520px;background:linear-gradient(160deg,#8f8371,var(--warm-grey) 45%,var(--warm-grey-dark));padding-top:58px}
.products .section-title{color:var(--white)}
.product-grid{display:grid;grid-template-columns:repeat(4,1fr);gap:28px;padding:0 180px;margin-top:46px}
.product{text-align:center}
.product-card{background:var(--white);height:150px;border-radius:3px;display:flex;flex-direction:column;align-items:center;justify-content:center;gap:12px;box-shadow:0 3px 10px rgba(0,0,0,.18)}
.product-card h3{font-size:13px;font-weight:700;color:var(--ink);line-height:1.35;padding:0 10px}
.product p{font-size:12px;line-height:1.6;color:#f3efe9;margin:16px 6px 12px}

/* Partners */
.partners{height:100px;display:flex;align-items:center;justify-content:center;gap:70px;background:var(--white)}
.badge{background:#d8d2c9;border-radius:3px}

/* Footer */
.site-footer{height:200px;background:var(--footer);padding:34px 56px 0;display:grid;grid-template-columns:1.2fr 1fr 1fr 1fr;gap:40px;color:#b8aea2}
.site-footer h4{color:var(--white);font-size:14px;font-weight:700;margin-bottom:12px}
.site-footer p,.site-footer li{font-size:11.5px;line-height:1.7;list-style:none}
.footer-bottom{height:40px;background:var(--footer-deep);display:flex;align-items:center;padding:0 56px;color:#9c9185;font-size:11px}
.social{margin-left:auto;display:flex;gap:10px}
.social span{width:14px;height:14px;border-radius:50%;background:#9c9185}
</style>
</head>
<body>

<header class="site-header">
  <a class="brand" href="#">Veyra</a>
  <nav class="main-nav">
    <a href="#">IT support</a><a href="#">VoIP</a><a href="#">Internet and Data</a><a href="#">Cloud hosting</a><a href="#">About</a><a href="#">Contact</a>
  </nav>
  <div class="header-contact">
    <span class="phone">
      <svg width="14" height="14" viewBox="0 0 24 24"><path d="M6.6 10.8a15 15 0 0 0 6.6 6.6l2.2-2.2a1 1 0 0 1 1-.25 11.4 11.4 0 0 0 3.6.57 1 1 0 0 1 1 1V20a1 1 0 0 1-1 1A17 17 0 0 1 3 4a1 1 0 0 1 1-1h3.5a1 1 0 0 1 1 1c0 1.25.2 2.45.57 3.57a1 1 0 0 1-.25 1z" fill="#877a69"/></svg>
      02 5550 1847
    </span>
    <a class="login-btn" href="#">
      <svg width="11" height="13" viewBox="0 0 12 14"><rect x="1" y="6" width="10" height="8" rx="1" fill="#fff"/><path d="M3 6V4a3 3 0 0 1 6 0v2" stroke="#fff" stroke-width="1.6" fill="none"/></svg>
      LOGIN
    </a>
  </div>
</header>

<section class="hero">
  <div class="hero-photo" role="img" aria-label="Business person in a white shirt walking outdoors under autumn trees, holding a framed cloud icon"></div>
  <h1 class="hero-title">do IT better</h1>
  <div class="hero-dots"><span class="active"></span><span></span><span></span></div>
</section>

<section class="services">
  <h2 class="section-title">SERVICES WE OFFER</h2>
  <div class="service-grid">
    <div class="service">
      <svg viewBox="0 0 100 90"><rect x="18" y="14" width="64" height="44" rx="3" fill="none" stroke="#877a69" stroke-width="4"/><rect x="40" y="58" width="20" height="10" fill="#877a69"/><rect x="30" y="68" width="40" height="4" fill="#877a69"/><circle cx="50" cy="36" r="10" fill="none" stroke="#e8862a" stroke-width="4"/></svg>
      <h3>Hardware Software Support</h3>
      <p>We supply, configure and install hardware to cope with very high demands, and undo.</p>
      <a class="read-more" href="#">READ MORE ›</a>
    </div>
    <div class="service">
      <svg viewBox="0 0 100 90"><rect x="14" y="20" width="44" height="34" rx="3" fill="none" stroke="#877a69" stroke-width="4"/><rect x="26" y="54" width="20" height="8" fill="#877a69"/><rect x="62" y="26" width="24" height="42" rx="3" fill="none" stroke="#e8862a" stroke-width="4"/><circle cx="74" cy="60" r="2.5" fill="#e8862a"/></svg>
      <h3>Data and Voice</h3>
      <p>We supply, configure and install hardware to cope with very high demands, and undo.</p>
      <a class="read-more" href="#">READ MORE ›</a>
    </div>
    <div class="service">
      <svg viewBox="0 0 100 90"><path d="M28 56a14 14 0 0 1 2-28 20 20 0 0 1 38 4 12 12 0 0 1 2 24z" fill="none" stroke="#877a69" stroke-width="4"/><path d="M50 40v36M40 66l10 10 10-10" fill="none" stroke="#e8862a" stroke-width="4"/></svg>
      <h3>Cloud Services</h3>
      <p>We supply, configure and install hardware to cope with very high demands, and undo.</p>
      <a class="read-more" href="#">READ MORE ›</a>
    </div>
    <div class="service">
      <svg viewBox="0 0 100 90"><path d="M24 52V42a26 26 0 0 1 52 0v10" fill="none" stroke="#877a69" stroke-width="4"/><rect x="18" y="46" width="14" height="22" rx="4" fill="#e8862a"/><rect x="68" y="46" width="14" height="22" rx="4" fill="#e8862a"/><path d="M75 68q0 10-18 10" fill="none" stroke="#877a69" stroke-width="3"/></svg>
      <h3>Support</h3>
      <p>We supply, configure and install hardware to cope with very high demands, and undo.</p>
      <a class="read-more" href="#">READ MORE ›</a>
    </div>
  </div>
</section>

<section class="outsourcing">
  <h2>IT OUTSOURCING THE WAY IT SHOULD BE</h2>
  <div class="outsourcing-body">
    <div class="outsourcing-copy">
      <h3>The Right People</h3>
      <p>Not only does Veyra have highly qualified people with certifications across all major vendors, but importantly we speak plain English and translate IT questions into a language you can understand and make decisions easily.</p>
      <p>We pride ourselves in our skill, integrity and ability to think and act in your best interests – that's what gives us customers who stay with us over time.</p>
      <a class="btn-grey" href="#">READ MORE</a>
    </div>
    <div class="video" role="img" aria-label="Video still of a team seen from above around a table holding puzzle pieces">
      <svg class="play" width="64" height="64" viewBox="0 0 64 64"><circle cx="32" cy="32" r="30" fill="rgba(255,255,255,.25)" stroke="#fff" stroke-width="2"/><path d="M26 20l20 12-20 12z" fill="#fff"/></svg>
    </div>
  </div>
</section>

<section class="products">
  <h2 class="section-title">WE PROVIDE BEST PRODUCTS</h2>
  <div class="product-grid">
    <div class="product">
      <div class="product-card">
        <svg width="52" height="44" viewBox="0 0 52 44"><rect x="3" y="3" width="46" height="30" rx="2" fill="none" stroke="#877a69" stroke-width="3"/><rect x="18" y="33" width="16" height="6" fill="#877a69"/><rect x="12" y="39" width="28" height="3" fill="#e8862a"/></svg>
        <h3>Corporate<br>Workstations</h3>
      </div>
      <p>Robust business grade performance and reliability. Why choose any other PC.</p>
      <a class="read-more" href="#">READ MORE ›</a>
    </div>
    <div class="product">
      <div class="product-card">
        <svg width="56" height="44" viewBox="0 0 56 44"><rect x="8" y="6" width="40" height="26" rx="2" fill="none" stroke="#877a69" stroke-width="3"/><path d="M2 36h52l-4 5H6z" fill="#e8862a"/></svg>
        <h3>Orin Desk, Orin Book,<br>Orin Pad &amp; Orin Phone</h3>
      </div>
      <p>Great for home and the office. Stylish, simple and capable. You can easily integrate.</p>
      <a class="read-more" href="#">READ MORE ›</a>
    </div>
    <div class="product">
      <div class="product-card">
        <svg width="48" height="46" viewBox="0 0 48 46"><rect x="4" y="3" width="40" height="12" rx="2" fill="none" stroke="#877a69" stroke-width="3"/><rect x="4" y="17" width="40" height="12" rx="2" fill="none" stroke="#877a69" stroke-width="3"/><rect x="4" y="31" width="40" height="12" rx="2" fill="none" stroke="#877a69" stroke-width="3"/><circle cx="36" cy="9" r="2" fill="#e8862a"/><circle cx="36" cy="23" r="2" fill="#e8862a"/><circle cx="36" cy="37" r="2" fill="#e8862a"/></svg>
        <h3>Norvex Standalone &amp;<br>Blade Servers</h3>
      </div>
      <p>The only serious choice in servers, multiple distributed and redundant systems.</p>
      <a class="read-more" href="#">READ MORE ›</a>
    </div>
    <div class="product">
      <div class="product-card">
        <svg width="50" height="46" viewBox="0 0 50 46"><rect x="13" y="3" width="24" height="12" fill="none" stroke="#877a69" stroke-width="3"/><rect x="3" y="15" width="44" height="18" rx="2" fill="none" stroke="#877a69" stroke-width="3"/><rect x="13" y="28" width="24" height="15" fill="#fff" stroke="#e8862a" stroke-width="3"/></svg>
        <h3>Norvex &amp; Kaltro<br>Printers</h3>
      </div>
      <p>Stay right, buy once. Don't muck around with low-priced inkjet refills and lower quality.</p>
      <a class="read-more" href="#">READ MORE ›</a>
    </div>
  </div>
</section>

<section class="partners" aria-label="Partner certifications">
  <span class="badge" style="width:80px;height:28px"></span>
  <span class="badge" style="width:26px;height:30px"></span>
  <span class="badge" style="width:62px;height:34px"></span>
  <span class="badge" style="width:46px;height:46px"></span>
</section>

<footer class="site-footer">
  <div>
    <h4>About Company</h4>
    <p>Servicing mid-sized business IT needs with experience in enterprise technologies and platforms, with a focus on customer returns.</p>
  </div>
  <div>
    <h4>Our Services</h4>
    <ul><li>Hardware Software Support</li><li>Data and Voice</li><li>Cloud Services</li><li>Support</li></ul>
  </div>
  <div>
    <h4>Products</h4>
    <ul><li>Corporate Workstations</li><li>Orin Desk, Book, Pad and Phone</li><li>Norvex Standalone and Blade Servers</li><li>Norvex and Kaltro Printers</li></ul>
  </div>
  <div>
    <h4>Remote</h4>
  </div>
</footer>
<div class="footer-bottom">
  <span>© 2017 Veyra. Terms of Use | Privacy | Sitemap</span>
  <div class="social"><span></span><span></span></div>
</div>

</body>
</html>
```